Flyer Design Project

I need to create a flyer to advertise an Luxury Self Catering Apartment Complex in a Ski Resort in Europe. The development offers luxury accommodation to those who are on a budget.

Below is what needs to be included and a basic layout design idea i had that can be changed. The information is important. Hoping to get it on a flyer sized 21.6 x 14 cm

Title - 'Luxury Self Catering Ski Apartments For Rent'
Sub Title - 'Located 200m from Gondola, Restaurants and Bars'

Studio - Sleeps 1-2 - From only £200 per week
1 Bed - Sleeps 2-4 - From only £250 per week
2 Bed - Sleeps 4-6 - From only £350 per week

Image 1 Image 2 Image 3

- Fully Furnished Modern, Spacious & Comfortable Apartments
- Fully Staffed Development (Reception, Bar + Daily Cleaning)
- Family friendly & suitable for children of all ages

(Chirplo Icon) @snowhavenvarno
E-mail - snowhavenvarno@mailnest.co.uk
Telephone - +44 (0) 7831 602 948

Target Market(s)

Our target market is very wide. We are trying to attract students, couples and families who are skiing on a budget.

Industry/Entity Type

Accommodation

Requirements
Must have
• The text contained in 'task description' is important but i'd like to be led on design. Size of around 21.6 x 14cm is important and i'd like the 3 images below (hopefully someone can get of the date and time in orange bottom right of all pics)

http://i2207.picstorra.com/albums/bq384/rtmpics/Varno/512_00_640_zpsa4c9e13f.jpeg

http://i2207.picstorra.com/albums/bq384/rtmpics/Varno/b_02_zps1846acd2.jpeg

http://i2207.picstorra.com/albums/bq384/rtmpics/Varno/512_08_640_zps9e3d70b4.jpeg

```html
<!DOCTYPE html>
<html lang="en">
<head>
<meta charset="utf-8">
<title>Luxury Self Catering Ski Apartments – Flyer</title>
<link rel="stylesheet" href="https://fonts.googleapis.com/css2?family=Oswald:wght@300;500&family=Titan+One&family=Open+Sans:wght@400;700&family=PT+Serif&display=swap">
<style>
:root{
  --page:#ece8e2;
  --maroon:#5a1416;
  --maroon-deep:#3e0c0d;
  --gold:#d99a3a;
  --gold-light:#f0c06a;
  --cream:#fbefd8;
  --cream-deep:#f3dcae;
  --ink:#4a1010;
  --white:#ffffff;
}
*{margin:0;padding:0;box-sizing:border-box}
html,body{width:1200px;height:900px;overflow:hidden;background:var(--page)}
.flyer{position:absolute;left:305px;top:32px;width:530px;height:820px;overflow:hidden;
  background:linear-gradient(180deg,var(--cream) 0%,var(--cream-deep) 100%);
  box-shadow:0 6px 18px rgba(0,0,0,.25)}
.building-photo{position:absolute;left:0;top:90px;width:530px;height:330px;
  background:linear-gradient(180deg,#f4f4f4 0%,#c9c2b8 35%,#8a6b52 70%,#5a4636 100%)}
.waves{position:absolute;left:0;top:0;width:530px;height:820px}
.title{position:absolute;top:26px;left:0;width:100%;text-align:center;
  font-family:"Oswald",sans-serif;font-weight:500;font-size:27px;line-height:36px;color:var(--gold-light);letter-spacing:.2px}
.subtitle{position:absolute;top:62px;left:0;width:100%;text-align:center;
  font-family:"Oswald",sans-serif;font-weight:300;font-size:21px;line-height:28px;color:var(--white)}
.thumb{position:absolute;left:15px;width:142px;border:4px solid var(--gold);
  box-shadow:0 2px 5px rgba(0,0,0,.3)}
.thumb-bedroom{top:438px;height:84px;background:linear-gradient(135deg,#6b4a36,#d8c7ae 55%,#f2ebe0)}
.thumb-lounge{top:544px;height:88px;background:linear-gradient(135deg,#e9e4dc,#8b6f5a 60%,#3b2a20)}
.thumb-kitchen{top:648px;height:88px;background:linear-gradient(135deg,#2e211b,#7a5a45 55%,#e6dfd4)}
.details{position:absolute;left:180px;top:426px;width:340px;color:var(--ink)}
.location{text-align:center;font-family:"Titan One",sans-serif;font-weight:400;font-size:23px;line-height:30px;color:var(--maroon-deep);margin-left:-10px}
.award{text-align:center;font-family:"Open Sans",sans-serif;font-weight:700;font-size:13.5px;line-height:17px;color:var(--maroon-deep);margin-left:-10px}
.quote{margin-top:10px;width:290px;font-family:"PT Serif",serif;font-size:14.5px;line-height:17px}
.features{list-style:none;font-family:"PT Serif",serif;font-size:14.5px;line-height:16.5px}
.amenities{margin-top:12px}
.features li{position:relative;padding-left:19px;margin-bottom:4px}
.features li::before{content:"➤";position:absolute;left:0;top:0;color:var(--maroon-deep);font-size:13px}
.rates{margin-top:10px}
.rates li{margin-bottom:3.5px}
.rates strong{font-family:"Open Sans",sans-serif;font-weight:700}
.contact{position:absolute;left:52px;top:760px;font-family:"Open Sans",sans-serif;font-size:14px;line-height:18px;color:var(--white)}
.contact-row{display:flex;align-items:center;gap:6px}
.contact-row svg{flex:none}
.chirplo-mark{display:inline-block;width:11px;height:11px;background:var(--gold);margin-left:8px}
</style>
</head>
<body>
<main class="flyer">
  <div class="building-photo" role="img" aria-label="Photograph of the stone and white rendered apartment building with balconies and mountains behind"></div>

  <svg class="waves" viewBox="0 0 530 820" aria-hidden="true">
    <path d="M90 128C250 142 420 112 530 84V100C420 130 260 156 120 146C105 142 96 136 90 128Z" fill="var(--gold)"/>
    <path d="M0 0H530V92C430 118 300 138 180 134C110 132 50 150 0 170Z" fill="var(--maroon)"/>
    <path d="M0 410C120 395 260 392 380 396C450 398 500 392 530 380V820H0Z" fill="var(--cream)"/>
    <path d="M0 405C150 390 300 388 420 393C470 395 505 388 530 372V384C500 400 460 405 400 404C270 400 120 402 0 422Z" fill="var(--gold)" opacity=".9"/>
    <path d="M0 748C150 740 360 742 530 770V820H0Z" fill="var(--maroon)"/>
    <path d="M0 742C160 734 360 738 530 764V770C360 744 160 742 0 750Z" fill="var(--gold)"/>
  </svg>

  <h1 class="title">Luxury Self Catering Ski Apartments For Rent</h1>
  <p class="subtitle">Located 200m from Gondola, Restaurants and Bars</p>

  <div class="thumb thumb-bedroom" role="img" aria-label="Photograph of an apartment bedroom with double bed"></div>
  <div class="thumb thumb-lounge" role="img" aria-label="Photograph of an apartment lounge with sofa and armchair"></div>
  <div class="thumb thumb-kitchen" role="img" aria-label="Photograph of an apartment kitchen and dining table"></div>

  <section class="details">
    <h2 class="location">Varno - Bulgaria</h2>
    <p class="award">TripTally<br>Best Value Ski Resort in Europe 2011 + 2012</p>
    <p class="quote">The Daily Ledger<br>Varno has been transformed into a winter destination that can truly compete with the Alps - at a fraction of the cost.</p>
    <ul class="features amenities">
      <li>Fully Furnished Modern,<br>Spacious &amp; Comfortable Apartments</li>
      <li>Fully Staffed Development<br>(Reception, Bar + Daily Cleaning)</li>
      <li>Family friendly &amp; suitable for children of all ages</li>
    </ul>
    <ul class="features rates">
      <li>Studio - Sleeps 1-2 - From only <strong>£200</strong> per week</li>
      <li>1 Bed - Sleeps 2-4 - From only <strong>£250</strong> per week</li>
      <li>2 Bed - Sleeps 4-6 - From only <strong>£350</strong> per week</li>
    </ul>
  </section>

  <footer class="contact">
    <p>CONTACT US :</p>
    <p class="contact-row">
      <svg width="11" height="11" viewBox="0 0 24 24"><path d="M6.6 10.8a15 15 0 0 0 6.6 6.6l2.2-2.2a1 1 0 0 1 1-.25 11 11 0 0 0 3.6.57 1 1 0 0 1 1 1V20a1 1 0 0 1-1 1A17 17 0 0 1 3 4a1 1 0 0 1 1-1h3.5a1 1 0 0 1 1 1c0 1.25.2 2.45.57 3.57a1 1 0 0 1-.25 1Z" fill="var(--gold)"/></svg>
      +44 (0) 7831 602 948
    </p>
    <p class="contact-row">
      <svg width="11" height="9" viewBox="0 0 22 16"><rect width="22" height="16" rx="1" fill="var(--gold)"/><path d="M1 1l10 8 10-8" stroke="var(--maroon)" stroke-width="1.6" fill="none"/></svg>
      snowhavenvarno@mailnest.co.uk
      <span class="chirplo-mark" aria-label="Chirplo"></span>
      @snowhavenvarno
    </p>
  </footer>
</main>
</body>
</html>
```